New Organic Skin Care Line Needs to Design a Product Label

***THE WINNER OF THIS PROJECT WILL MOST LIKELY BECOME THE EXCLUSIVE DESIGNER FOR OUR OTHER PRODUCT LABELS***

We need a label design for a new organic skin care product line called "Maple Dune Festoon." This specific product is a 100% pure organic coconut oil. It's used for skin hydration, protection, and makeup removal.

Info to include on front label:

1. Logo: Maple Dune Festoon (attached)
2. Product Name: Pure Coconut Oil (emphasize "organic" somewhere)
3. Slogan: Hydrate your skin and hair.
4. Size: 8 FL OZ 236mL

Attached is:

1. The brand logo "Maple Dune Festoon" with a white background.
2. An image of the bottle we will use.
3. An image of the bottle with lines to show the size and placement of the label.
4. The brand logo "Maple Dune Festoon" with a black background. (photoshop file)

What we need:

A simple mock up of the front side of the label on the bottle. We first want to know what it will look like on the bottle given the size and dimensions.

- We would like one label with a white background (including the logo with a white background).
- We would like a second label with a black background (including the logo with a black background, just need to make the black font white instead of black).

We can get a great idea of what to expect from the front side of the label so we will complete the back side once we identify a winner.
Updates

Apologies, but we are now using a different bottle. The previous one is now discontinued. Please view the two most recent images uploaded. One is an image of the new bottle by itself. The other is an image of that bottle with instructions. Please use your most recent designs on the new bottle. Feel free to make any modifications you see fit to compliment the new bottle shape. Added Friday, March 18, 2016

Project Deadline Extended
Reason: We are still working with the label company to finalize the size. Once the size is confirmed we will have to tweak labels based on finalized measurements.

Target Market(s)

Women, 18-70

Industry/Entity Type

Skin Care Product

Font styles to use
Decorative
Script

Requirements
Must have
• -"shabby sheek" and "cute" theme
• -soft organic feel
• -the ingredients are organic, pure, and natural. That should be an essence of the label.

```html
<!DOCTYPE html>
<html lang="en">
<head>
<meta charset="utf-8">
<title>Maple Dune Festoon – Pure Coconut Oil Label</title>
<link rel="stylesheet" href="https://fonts.googleapis.com/css2?family=EB+Garamond:wght@400;500&family=Questrial&display=swap">
<style>
  :root {
    --canvas-bg: #ffffff;
    --label-black: #1f1f1f;
    --label-ink: #ffffff;
    --ornament-tone: #5a5a5a;
  }
  * { margin: 0; padding: 0; box-sizing: border-box; }
  html, body {
    width: 716px;
    height: 1200px;
    overflow: hidden;
    background: var(--canvas-bg);
  }
  .label-art {
    position: absolute;
    left: 0;
    top: 0;
    width: 716px;
    height: 1200px;
    display: block;
  }
  .label-shape { fill: var(--label-black); }
  .brand-name {
    font-family: "EB Garamond", Georgia, serif;
    font-size: 13.5px;
    letter-spacing: 1.6px;
    fill: var(--label-ink);
  }
  .divider { stroke: var(--label-ink); stroke-width: 1.6; }
  .product-name {
    font-family: "EB Garamond", Georgia, serif;
    font-weight: 500;
    font-size: 21px;
    letter-spacing: 0.3px;
    fill: var(--label-ink);
  }
  .slogan {
    font-family: "EB Garamond", Georgia, serif;
    font-size: 11.5px;
    letter-spacing: 0.4px;
    fill: var(--label-ink);
  }
  .organic-claim {
    font-family: "Questrial", Arial, sans-serif;
    font-size: 20px;
    letter-spacing: 0.5px;
    fill: var(--label-ink);
  }
  .volume {
    font-family: "Questrial", Arial, sans-serif;
    font-size: 11px;
    letter-spacing: 0.6px;
    fill: var(--label-ink);
  }
  .botanical-sprig { fill: var(--ornament-tone); }
</style>
</head>
<body>
<svg class="label-art" viewBox="0 0 716 1200" xmlns="http://www.w3.org/2000/svg">
  <path class="label-shape" d="M180,1010 C170,980 195,955 215,945 C190,925 175,895 200,875 C220,860 240,868 250,875 C230,850 225,815 245,790 C255,772 272,775 280,780 C275,745 290,712 330,700 C365,690 385,715 392,730 C402,700 432,690 458,700 C492,714 492,745 482,770 C512,770 542,790 532,820 C522,850 497,856 480,860 C507,870 535,880 542,902 C546,927 520,950 497,960 C517,975 532,1000 522,1020 C507,1045 472,1046 450,1036 C420,1030 300,1046 222,1042 C198,1040 186,1026 180,1010 Z"/>

  <text class="brand-name" x="361" y="824" text-anchor="middle">MAPLE DUNE FESTOON</text>

  <rect class="botanical-sprig" x="262" y="846" width="170" height="56" rx="22" role="img" aria-label="Line drawing of two leaves and a small flowering sprig"/>

  <line class="divider" x1="265" y1="911" x2="470" y2="911"/>
  <text class="product-name" x="362" y="934" text-anchor="middle">PURE COCONUT OIL</text>
  <line class="divider" x1="248" y1="942" x2="478" y2="942"/>
  <text class="slogan" x="362" y="966" text-anchor="middle">HYDRATE YOUR SKIN AND HAIR</text>

  <text class="organic-claim" x="232" y="1030">ORGANIC</text>
  <text class="volume" x="378" y="1028">236 ML</text>
</svg>
</body>
</html>
```